Integrated content management graphic

We are looking for a creative iteration for the attached file. We are currently in the process of renewing our branding and this graphic will be a center piece to our product marketing. Our website is www.brelvonvista.com for more information on products and company.
Future projects are available for designers submitting outstanding concepts and branding capability.
Updates

Project Deadline Extended
Reason: We are in the process of picking our final two.

Target Market(s)

Audience is IT and anyone interested in integrating content management with their ERP/Accounting system.

Industry/Entity Type

Construction

Requirements
Must have
• The design must use the current color scheme associated with our website, yellow, black, grey. White can also be used. The design should be sleek.
Nice to have
• 3D Feel. The wheel could take on a stadium concept in 3d.

```html
<!DOCTYPE html>
<html lang="en">
<head>
<meta charset="utf-8">
<title>Integrated Content Management Wheel</title>
<link href="https://fonts.googleapis.com/css2?family=Arimo:wght@400;700&display=swap" rel="stylesheet">
<style>
  :root {
    --bg: #f3efd9;
    --outer-fill: #4a4536;
    --outer-edge: #2f2b21;
    --outer-text: #f2d31b;
    --mid-fill: #efd20e;
    --mid-edge: #c9ad05;
    --mid-text: #8a8878;
    --inner-fill: #b3b3ae;
    --inner-edge: #86867f;
    --inner-text: #45443d;
    --hub-fill: #3d3a2d;
    --hub-ring: #8f8c80;
    --hub-text: #f2d31b;
  }
  html, body {
    margin: 0;
    padding: 0;
    width: 1200px;
    height: 900px;
    overflow: hidden;
    background: var(--bg);
  }
  .wheel {
    display: block;
    width: 1200px;
    height: 900px;
    font-family: "Arimo", Arial, sans-serif;
  }
  .segment { stroke: var(--bg); stroke-width: 10; stroke-linejoin: round; }
  .segment--outer { fill: var(--outer-fill); }
  .segment--mid { fill: var(--mid-fill); }
  .segment--inner { fill: var(--inner-fill); }
  .rim--outer { fill: none; stroke: var(--outer-edge); stroke-width: 3; }
  .rim--mid { fill: none; stroke: var(--mid-edge); stroke-width: 3; }
  .rim--inner { fill: none; stroke: var(--inner-edge); stroke-width: 3; }
  .label { text-anchor: middle; dominant-baseline: central; }
  .label--outer { fill: var(--outer-text); font-size: 40px; }
  .label--mid { fill: var(--mid-text); font-size: 32px; }
  .label--inner { fill: var(--inner-text); font-size: 24px; }
  .hub { fill: var(--hub-fill); stroke: var(--hub-ring); stroke-width: 8; }
  .hub-name { fill: var(--hub-text); font-weight: 700; font-size: 30px; text-anchor: middle; }
</style>
</head>
<body>
<svg class="wheel" viewBox="0 0 1200 900" xmlns="http://www.w3.org/2000/svg" role="img" aria-label="Brelvon Vista content management wheel">
  <defs>
    <!-- text guides: outer ring -->
    <path id="guide-property" d="M243.0 525.9 A365 365 0 0 1 463.3 111.6"/>
    <path id="guide-accounting" d="M463.3 111.6 A365 365 0 0 1 736.7 111.6"/>
    <path id="guide-project" d="M736.7 111.6 A365 365 0 0 1 947.2 337.2"/>
    <path id="guide-equipment" d="M736.7 788.4 A365 365 0 0 0 947.2 337.2"/>
    <path id="guide-hr" d="M463.3 788.4 A365 365 0 0 0 736.7 788.4"/>
    <path id="guide-facilities" d="M243.0 525.9 A365 365 0 0 0 463.3 788.4"/>
    <!-- text guides: middle ring -->
    <path id="guide-office" d="M365.1 364.5 A250 250 0 0 1 717.4 229.3"/>
    <path id="guide-erp" d="M717.4 229.3 A250 250 0 0 1 849.1 428.2"/>
    <path id="guide-pms" d="M423.2 626.8 A250 250 0 0 0 849.1 428.2"/>
    <path id="guide-vault" d="M423.2 626.8 A250 250 0 0 1 365.1 364.5"/>
    <!-- text guides: inner ring -->
    <path id="guide-capture" d="M493.9 343.9 A150 150 0 0 1 706.1 343.9"/>
    <path id="guide-doc-top" d="M716.7 333.3 A165 165 0 0 1 716.7 566.7"/>
    <path id="guide-doc-bottom" d="M693.3 356.7 A132 132 0 0 1 693.3 543.3"/>
    <path id="guide-workflow" d="M493.9 556.1 A150 150 0 0 0 706.1 556.1"/>
    <path id="guide-archiving" d="M493.9 556.1 A150 150 0 0 1 493.9 343.9"/>
  </defs>

  <g class="ring ring--outer">
    <path class="segment segment--outer" d="M194.1 536.3 A415 415 0 0 1 444.5 65.2 L482.0 157.9 A315 315 0 0 0 291.9 515.5 Z"/>
    <path class="segment segment--outer" d="M444.5 65.2 A415 415 0 0 1 755.5 65.2 L718.0 157.9 A315 315 0 0 0 482.0 157.9 Z"/>
    <path class="segment segment--outer" d="M755.5 65.2 A415 415 0 0 1 994.7 321.8 L899.6 352.7 A315 315 0 0 0 718.0 157.9 Z"/>
    <path class="segment segment--outer" d="M994.7 321.8 A415 415 0 0 1 755.5 834.8 L718.0 742.1 A315 315 0 0 0 899.6 352.7 Z"/>
    <path class="segment segment--outer" d="M755.5 834.8 A415 415 0 0 1 444.5 834.8 L482.0 742.1 A315 315 0 0 0 718.0 742.1 Z"/>
    <path class="segment segment--outer" d="M444.5 834.8 A415 415 0 0 1 194.1 536.3 L291.9 515.5 A315 315 0 0 0 482.0 742.1 Z"/>
    <text class="label label--outer"><textPath href="#guide-property" startOffset="50%">Property Mgmt</textPath></text>
    <text class="label label--outer"><textPath href="#guide-accounting" startOffset="50%">Accounting</textPath></text>
    <text class="label label--outer"><textPath href="#guide-project" startOffset="50%">Project Mgmt</textPath></text>
    <text class="label label--outer"><textPath href="#guide-equipment" startOffset="50%">Equipment Mgmt</textPath></text>
    <text class="label label--outer"><textPath href="#guide-hr" startOffset="50%">HR</textPath></text>
    <text class="label label--outer"><textPath href="#guide-facilities" startOffset="50%">Facilities Mgmt</textPath></text>
  </g>

  <g class="ring ring--mid">
    <path class="segment segment--mid" d="M322.8 349.1 A295 295 0 0 1 738.5 189.5 L696.2 269.0 A205 205 0 0 0 407.4 379.9 Z"/>
    <path class="segment segment--mid" d="M738.5 189.5 A295 295 0 0 1 893.9 424.3 L804.2 432.1 A205 205 0 0 0 696.2 269.0 Z"/>
    <path class="segment segment--mid" d="M893.9 424.3 A295 295 0 0 1 391.4 658.6 L455.0 595.0 A205 205 0 0 0 804.2 432.1 Z"/>
    <path class="segment segment--mid" d="M391.4 658.6 A295 295 0 0 1 322.8 349.1 L407.4 379.9 A205 205 0 0 0 455.0 595.0 Z"/>
    <text class="label label--mid"><textPath href="#guide-office" startOffset="50%">Deskline Office</textPath></text>
    <text class="label label--mid"><textPath href="#guide-erp" startOffset="50%">ERP</textPath></text>
    <text class="label label--mid"><textPath href="#guide-pms" startOffset="50%">Project Mgmt Software</textPath></text>
    <text class="label label--mid"><textPath href="#guide-vault" startOffset="50%">TeamVault</textPath></text>
  </g>

  <g class="ring ring--inner">
    <path class="segment segment--inner" d="M462.1 312.1 A195 195 0 0 1 737.9 312.1 L674.2 375.8 A105 105 0 0 0 525.8 375.8 Z"/>
    <path class="segment segment--inner" d="M737.9 312.1 A195 195 0 0 1 737.9 587.9 L674.2 524.2 A105 105 0 0 0 674.2 375.8 Z"/>
    <path class="segment segment--inner" d="M737.9 587.9 A195 195 0 0 1 462.1 587.9 L525.8 524.2 A105 105 0 0 0 674.2 524.2 Z"/>
    <path class="segment segment--inner" d="M462.1 587.9 A195 195 0 0 1 462.1 312.1 L525.8 375.8 A105 105 0 0 0 525.8 524.2 Z"/>
    <text class="label label--inner"><textPath href="#guide-capture" startOffset="50%">Capture</textPath></text>
    <text class="label label--inner"><textPath href="#guide-doc-top" startOffset="50%">Document</textPath></text>
    <text class="label label--inner"><textPath href="#guide-doc-bottom" startOffset="50%">Management</textPath></text>
    <text class="label label--inner"><textPath href="#guide-workflow" startOffset="50%">Workflow</textPath></text>
    <text class="label label--inner"><textPath href="#guide-archiving" startOffset="50%">Archiving</textPath></text>
  </g>

  <g class="hub-group">
    <circle class="hub" cx="600" cy="450" r="92"/>
    <text class="hub-name" x="600" y="444">Brelvon</text>
    <text class="hub-name" x="600" y="480">Vista</text>
  </g>
</svg>
</body>
</html>
```